Lawn Maintenance Company needs Flyer (Postcard) Design.

Hi everyone.
The majority of what I do is lawn maintenance (grass cutting and trimming/edging).

I'm pretty well open to anything (even humour) but want to stay away from the cartoon/illustration type flyer (but always receptive if you think you have something that might look good, like Pipkin (Thimbles character) :)
Simple but I guess as everyone, something that catches people's eye.

Feel free to kind of play with the name if you think it would help, I would be willing to pay extra if you thought you had a good idea for some type of logo also.

Flyer/Postcard will be front and back, front mainly outlined here, back would be a list of additional services.

Main points I want to get across.
- Professional
- Reliable
- Not like the larger companies that send students or part time
helpers
Kind of want to get those points across without necessarily saying them.

Ok, well, if you haven't rolled your eyes and headed off to the next project.................... :)

Target Market(s)

Mostly regular people with bungalow / two storey houses that don't want to do it themselves and want a nice lawn to frame their house.

Industry/Entity Type

It Company

Requirements
Must have
• Front
** Bramblecrest Landscaping and Lawn Services
** Lawn Maintenance
** (416) 555-3827
** bramblecrestyard@mailvora.com

Back
Commercial and Residential
Plaza Maintenance
Spring/Fall Clean-up
Fertilizing
Weed Prevention
Hedge Trimming
Flower Bed Design
Topdressing
Triplemix
Overseeding
Lawn & flower bed re-edging
Eavestrough Cleaning
Nice to have
• ummmm....grass. lol :)
Birds
Butterflies
Should not have
• Elaborate homes/gardens
Pictures/photos of people

**The pictures I have included are to just give you an idea of the work I do and the type of properties I do**
Please let me know if you want more pics.

```html
<!DOCTYPE html>
<html lang="en">
<head>
<meta charset="utf-8">
<title>Bramblecrest Landscaping and Lawn Services – Flyer Front</title>
<link rel="stylesheet" href="https://fonts.googleapis.com/css2?family=Cinzel:wght@700&family=Noto+Sans&family=Tinos&display=swap">
<style>
  :root {
    --paper: #ffffff;
    --forest: #0b6a36;
    --text-green: #1a6b3b;
    --headline-yellow: #f6ee1a;
    --glow: #d8e22a;
    --house-tint: rgba(242, 244, 198, 0.45);
    --ink: #1b1b1b;
    --mail-ink: #3a3a3a;
    --grass-light: #8fd14a;
    --grass-dark: #2f8a1e;
  }
  * { margin: 0; padding: 0; box-sizing: border-box; }
  html, body { width: 837px; height: 1200px; overflow: hidden; background: var(--paper); }
  .flyer { position: relative; width: 837px; height: 1200px; background: var(--paper); overflow: hidden; }

  .house-art {
    position: absolute; left: 70px; top: 172px; width: 690px; height: 928px;
    background: radial-gradient(ellipse at 50% 45%, var(--house-tint) 0%, rgba(242,244,198,0.2) 55%, rgba(242,244,198,0) 75%);
  }

  .title-band {
    position: absolute; left: 0; top: 36px; width: 837px; height: 108px;
    background: linear-gradient(90deg, var(--forest) 0%, var(--forest) 22%, var(--glow) 50%, var(--forest) 78%, var(--forest) 100%);
    display: flex; align-items: center; justify-content: center;
  }
  .title-band h2 {
    font-family: "Tinos", "Times New Roman", serif; font-weight: 400;
    font-size: 94px; color: var(--headline-yellow); line-height: 1; white-space: nowrap;
  }

  .butterfly { position: absolute; }
  .butterfly-green { left: 656px; top: 146px; width: 132px; height: 102px; }
  .butterfly-silver { left: 708px; top: 286px; width: 84px; height: 82px; }
  .butterfly-corner { left: 26px; top: 1050px; width: 84px; height: 74px; }

  .call-block {
    position: absolute; left: 0; width: 837px; top: 216px; text-align: center;
    font-family: "Noto Sans", Arial, sans-serif; color: var(--text-green); line-height: 1.2;
  }
  .call-block .call-label { font-size: 60px; padding-left: 10px; }
  .call-block .phone { font-size: 68px; margin-top: 2px; }

  .company-name {
    position: absolute; left: 0; width: 837px; top: 464px; text-align: center;
    font-family: "Cinzel", "Trajan Pro", serif; font-weight: 700;
    font-size: 78px; letter-spacing: 2px; line-height: 96px; color: var(--text-green);
    white-space: nowrap;
  }

  .tagline {
    position: absolute; left: 0; width: 837px; top: 880px; text-align: center;
    font-family: "Cinzel", "Trajan Pro", serif; font-weight: 700;
    font-size: 45px; letter-spacing: 1px; line-height: 56px; color: var(--ink);
  }

  .email {
    position: absolute; left: 137px; top: 1046px;
    font-family: "Noto Sans", Arial, sans-serif; font-size: 37px; letter-spacing: 0.5px;
    color: var(--mail-ink); white-space: nowrap;
  }

  .grass {
    position: absolute; left: 0; bottom: 0; width: 837px; height: 110px;
    background: linear-gradient(180deg, rgba(143,209,74,0) 0%, var(--grass-light) 35%, var(--grass-dark) 100%);
  }
</style>
</head>
<body>
<main class="flyer">
  <div class="house-art" role="img" aria-label="Faint outline illustration of a house behind the text"></div>

  <header class="title-band">
    <h2>Lawn Maintenance</h2>
  </header>

  <div class="butterfly butterfly-green" role="img" aria-label="Green butterfly illustration"
       style="background: radial-gradient(ellipse at 55% 50%, #c8e03a 0%, #5fa82a 55%, rgba(95,168,42,0) 72%);"></div>
  <div class="butterfly butterfly-silver" role="img" aria-label="Silver butterfly illustration"
       style="background: radial-gradient(ellipse at 50% 50%, #f4f4f4 0%, #8a8a8a 55%, rgba(138,138,138,0) 72%);"></div>

  <section class="call-block">
    <p class="call-label">Call</p>
    <p class="phone">(416) 555-3827</p>
  </section>

  <h1 class="company-name">Bramblecrest<br>Landscaping and<br>Lawn Services</h1>

  <p class="tagline">Quality affordable<br>lawn care</p>

  <div class="butterfly butterfly-corner" role="img" aria-label="Silver butterfly illustration"
       style="background: radial-gradient(ellipse at 50% 50%, #f4f4f4 0%, #8a8a8a 55%, rgba(138,138,138,0) 72%);"></div>

  <p class="email">bramblecrestyard@mailvora.com</p>

  <div class="grass" role="img" aria-label="Illustrated strip of green grass along the bottom edge"></div>
</main>
</body>
</html>
```